Commercial Flooring Contractor Website ($100 Bonus)

We are working with a new commercial flooring contractor in California. They work on schools, hospitals, and government projects.
A few websites for inspiration:
https://trimcoverwork.example (These guys are competitors and provide the same work our client does).
https://zqpavingsco.example (Although NOT a contractor, the simplicity of this site is stunning).
https://www.quietrapid.example (NOT a flooring contractor, but this site is modern, and has a boldness to it).
https://www.dawnfoldatelier.example/en-us (website for an Architectural office that is clean and showcases their work. I can see this working for a flooring contractor).
Thank you for taking the time to consider designing a website for us. We are web developers based in Stockton, CA, USA. Most of our projects go through the same process. Understanding this process may help you win a project with us. We custom-code all of our websites in-house. We don’t have any requirements as to what tools you use for your design, but we ask that you follow these guidelines.
IMAGES:
If you use any images or icons in the design, we ask that you have a link to the asset so we can purchase the image/icon. Most of the designs we submit do not have the customer’s images on them unless they have some great images. Be creative; show us the feeling you are trying to portray with your image choices. Use any royalty-free site you choose. We subscribe to Velto and mainly use their images, but we can purchase images outside of Velto.
FONTS:
We ask that you identify the fonts you’re using in the design. This can be done in a message if you want. We typically use Google Fonts and Velto Fonts.
CONTENT:
We're always open to different content and ideas. We often submit designs with stock images so the client can see our vision. We typically take pictures after the website launch to use their images with our vision. Lorem Ipsum is fine for paragraphs, but we ask that you make the Headers with correct English. We want to be able to show the vision and identify the sections of the website.
INSPIRATION:
We typically add a couple of links in the brief of websites we like to help you get started in your design.
REVISIONS:
We do not often ask for revisions of the designs unless we see something in the design that may not appeal to the client. If there are slight changes that we want to make, we do that in the development process.
FEEDBACK:
We rarely give feedback on designs during the design process. We are working on many website projects and do not have the time to provide feedback. We usually respond if your request is well thought out and asks specific questions, but a note asking “feedback, please” usually goes unanswered.
1 page

```html
<!DOCTYPE html>
<html lang="en">
<head>
<meta charset="utf-8">
<title>Corvane Flooring — Commercial Flooring Contractor</title>
<link href="https://fonts.googleapis.com/css2?family=Oswald:wght@500;600;700&family=Montserrat:wght@400;500;600&display=swap" rel="stylesheet">
<style>
:root{
  --red:#e8363d;
  --ink:#2b2b2b;
  --text:#555;
  --white:#fff;
  --mint:#e4efe4;
  --footer:#4a4c4b;
  --footer-deep:#262626;
  --display:'Oswald',sans-serif;
  --body:'Montserrat',sans-serif;
}
*{margin:0;padding:0;box-sizing:border-box}
html,body{width:1200px;height:3747px;overflow:hidden}
body{position:relative;font-family:var(--body);color:var(--text);background:var(--white)}
.abs{position:absolute}
.btn{position:absolute;display:flex;align-items:center;justify-content:center;background:var(--red);color:var(--white);border-radius:22px;font-family:var(--body);font-weight:500;font-size:15px;letter-spacing:2px;text-transform:uppercase;box-shadow:0 3px 8px rgba(0,0,0,.18)}
.photo{position:absolute}
.display{font-family:var(--display);font-weight:600;color:var(--ink)}
.display em{font-style:normal;color:var(--red)}

/* hero */
.hero{left:0;top:0;width:1200px;height:732px;background:linear-gradient(160deg,#6d6c69 0%,#4d4c4a 45%,#3a3937 100%)}
.nav{left:109px;top:28px;display:flex;gap:33px;font-size:14px;color:var(--white);font-weight:500}
.nav-rule{left:109px;top:76px;width:979px;height:1px;background:rgba(255,255,255,.45)}
.cta-top{left:857px;top:17px;width:231px;height:42px}
.brand-badge{left:487px;top:207px;width:226px;height:226px;border-radius:50%;background:var(--white);display:flex;align-items:center;justify-content:center;flex-direction:column;gap:10px}
.brand-badge .dot{width:18px;height:18px;border-radius:50%;background:var(--red)}
.brand-badge span{font-family:var(--body);font-weight:600;font-size:22px;color:var(--ink)}
.hero-title{left:200px;top:480px;width:800px;text-align:center;font-family:var(--display);font-weight:600;font-size:36px;line-height:57px;color:var(--white)}
.hero-line{left:599px;top:604px;width:2px;height:109px;background:var(--red)}
.socials{left:1068px;top:275px;display:flex;flex-direction:column;gap:8px}
.socials i{display:block;width:40px;height:40px;border-radius:50%;background:#4d7cc4;border:2px solid rgba(255,255,255,.7)}

/* about */
.about-photo{left:735px;top:640px;width:465px;height:493px;background:linear-gradient(180deg,#f4f5f6 0%,#dfe2e5 50%,#b9bdc1 100%)}
.stats{left:735px;top:1133px;width:465px;height:99px;background:var(--mint);display:flex;align-items:center;padding-left:18px}
.stat{display:flex;align-items:center;gap:12px}
.stat b{font-family:var(--display);font-weight:700;font-size:40px;color:var(--red)}
.stat span{font-size:15px;line-height:20px;color:#555}
.stat-divider{width:1px;height:44px;background:#c8d2c8;margin:0 14px}
.sec-head{display:flex;align-items:center;gap:32px}
.sec-head .rule{width:94px;height:2px;background:linear-gradient(90deg,var(--red) 50%,#ccc 50%)}
.sec-head h2{font-size:38px;line-height:1}
.about-head{left:110px;top:840px}
.about-copy{left:109px;top:903px;width:480px;font-size:16px;line-height:25.5px}
.about-copy p+p{margin-top:25px}
.about-copy em{font-style:normal;color:var(--red)}
.read-more{left:112px;top:1190px;width:162px;height:41px}

/* services */
.services{left:0;top:1345px;width:1200px;height:844px;background:linear-gradient(180deg,#8fa7b4 0%,#6f8a8f 35%,#6b7379 62%,#5c6166 100%)}
.svc-line{left:599px;top:1345px;width:2px;height:88px;background:var(--red)}
.svc-title{left:0;top:1455px;width:1200px;text-align:center;font-family:var(--display);font-weight:600;font-size:46px;color:var(--white)}
.svc-sub{left:0;top:1528px;width:1200px;text-align:center;font-family:var(--display);font-weight:600;font-size:26px;color:var(--white);text-transform:uppercase}
.svc-sub em{font-style:normal;color:var(--red)}
.svc-divider{top:1629px;width:1px;height:332px;background:rgba(255,255,255,.35)}
.svc{top:1634px;width:300px;text-align:center;color:var(--white)}
.svc .icon{margin:0 auto;width:136px;height:136px;border-radius:50%;background:var(--white);border:3px solid var(--red);display:flex;align-items:center;justify-content:center}
.svc .icon.active{background:var(--red);border-color:#fff}
.svc h3{margin-top:28px;font-weight:500;font-size:23px;letter-spacing:.5px}
.svc p{margin:10px auto 0;width:230px;font-size:13.5px;line-height:24px;color:rgba(255,255,255,.55)}
.svc a{display:inline-block;margin-top:2px;font-size:13.5px;color:rgba(255,255,255,.55);text-decoration:underline}
.svc a.lit{color:var(--white)}
.consult{left:484px;top:2044px;width:232px;height:40px}

/* projects */
.pillar-photo{left:0;top:2143px;width:340px;height:497px;background:linear-gradient(90deg,#d8dcd6 0%,#eef0ec 40%,#c9cfca 100%)}
.projects-head{left:618px;top:2343px}
.projects-copy{left:617px;top:2406px;width:480px;font-size:16px;line-height:26px}
.projects-copy strong{font-weight:500;color:#333}
.project-a{left:368px;top:2511px;width:464px;height:357px;background:linear-gradient(180deg,#dfe5ee 0%,#8fa1c2 50%,#eceef2 100%)}
.project-b{left:858px;top:2566px;width:342px;height:256px;background:linear-gradient(180deg,#e7f1f4 0%,#c6dbe2 55%,#e4ecee 100%)}
.view-more{left:484px;top:2916px;width:232px;height:40px}

/* footer */
.footer{left:0;top:3102px;width:1200px;height:415px;background:var(--footer)}
.foot-divider{top:3102px;width:1px;height:302px;background:rgba(255,255,255,.3)}
.foot-brand{left:110px;top:3190px;width:200px;height:160px;display:flex;flex-direction:column;align-items:center;justify-content:center;gap:12px}
.foot-brand .dot{width:18px;height:18px;border-radius:50%;background:var(--red)}
.foot-brand span{font-weight:600;font-size:22px;color:var(--white)}
.foot-h{top:3182px;font-family:var(--display);font-weight:600;font-size:17px;color:var(--white);text-transform:uppercase;padding-left:14px;border-left:3px solid var(--red)}
.foot-contact{left:380px;top:3232px;width:270px;color:var(--white);font-size:15.5px;line-height:22px}
.foot-contact li{list-style:none;display:flex;gap:18px;margin-bottom:18px}
.foot-contact svg{flex:none;margin-top:2px}
.foot-news{left:668px;top:3240px;width:290px;color:var(--white);font-size:14.5px;line-height:22px}
.email-field{left:667px;top:3300px;width:275px;height:41px;border-radius:21px;background:var(--white);color:#777;font-size:14px;display:flex;align-items:center;padding-left:17px}
.subscribe{left:667px;top:3356px;width:146px;height:40px}
.quick{left:1001px;top:3232px;color:var(--white);font-size:15.5px;line-height:29px;list-style:none}
.bottom{left:0;top:3517px;width:1200px;height:214px;background:var(--footer-deep)}
.bottom-social{left:509px;top:3610px;display:flex;gap:9px}
.bottom-social i{display:block;width:38px;height:38px;border-radius:50%;background:#3c79c8}
.legal{left:0;top:3663px;width:1200px;text-align:center;color:var(--white);font-size:16px}
.red-band{left:0;top:3731px;width:1200px;height:16px;background:var(--red)}
</style>
</head>
<body>

<!-- Hero -->
<section class="abs hero" role="img" aria-label="Photo of a modern glass-walled office interior with grey flooring"></section>
<nav class="abs nav"><span>HOME</span><span>ABOUT</span><span>SERVICES</span><span>NEWS</span><span>CONTACT US</span></nav>
<div class="btn cta-top">Free Consultation</div>
<div class="abs nav-rule"></div>
<div class="abs brand-badge"><div class="dot"></div><span>Corvane Flooring</span></div>
<h1 class="abs hero-title">Durable commercial floors built for<br>schools, hospitals and agencies</h1>
<div class="abs hero-line"></div>
<div class="abs socials" aria-label="Social links"><i></i><i></i><i></i><i></i></div>

<!-- About -->
<div class="photo about-photo" role="img" aria-label="Photo of an empty bright office space with a polished grey floor"></div>
<div class="abs stats">
  <div class="stat"><b>15+</b><span>Years Of<br>Experience</span></div>
  <div class="stat-divider"></div>
  <div class="stat"><b>150+</b><span>Completed<br>Projects</span></div>
</div>
<div class="abs sec-head about-head"><div class="rule"></div><h2 class="display">About <em>Corvane Flooring</em></h2></div>
<div class="abs about-copy">
  <p>Lorem Ipsum is simply dummy text of the printing and type-setting industry. Lorem Ipsum has been the industry's standard dummy text <em>ever since the 1500s,</em> when an unknown printer took a galley of type and scrambled it to make a type specimen book.</p>
  <p>It has survived not only five centuries, but also the leap into electronic typesetting, remaining essentially unchanged. It was popularised in the 1960s with the release of Letraset <em>sheets containing Lorem</em> Ipsum passages.</p>
</div>
<div class="btn read-more">Read More</div>

<!-- Services -->
<section class="abs services" role="img" aria-label="Photo of a glass office building with a stone-tiled plaza"></section>
<div class="abs svc-line"></div>
<h2 class="abs svc-title">What We Do</h2>
<p class="abs svc-sub">We are working with a new <em>commercial flooring contractor</em> in California.</p>
<div class="abs svc-divider" style="left:417px"></div>
<div class="abs svc-divider" style="left:784px"></div>

<div class="abs svc" style="left:83px">
  <div class="icon"><svg width="70" height="62" viewBox="0 0 70 62" fill="none" stroke="#333" stroke-width="3"><rect x="18" y="16" width="34" height="44"/><rect x="4" y="30" width="14" height="30"/><rect x="52" y="30" width="14" height="30"/><path d="M35 16V4h10v6H35"/><rect x="30" y="44" width="10" height="16"/><path d="M24 24h6M40 24h6M24 34h6M40 34h6M8 38h6M56 38h6M8 48h6M56 48h6"/></svg></div>
  <h3>SCHOOLS</h3>
  <p>Lorem ipsum is simply dummy text of the printing and typeset-ting industry. Lorem Ipsum has been the industry's</p>
  <a>Read More &gt;</a>
</div>
<div class="abs svc" style="left:450px">
  <div class="icon active"><svg width="64" height="66" viewBox="0 0 64 66" fill="none" stroke="#fff" stroke-width="3"><circle cx="32" cy="18" r="14"/><path d="M32 10v16M24 18h16"/><path d="M18 30H8v34h48V30H46"/><rect x="26" y="46" width="12" height="18"/><path d="M14 40h6M44 40h6M14 52h6M44 52h6"/></svg></div>
  <h3>HOSPITALS</h3>
  <p>Lorem Ipsum is simply dummy text of the printing and typeset-ting industry. Lorem Ipsum has been the industry's</p>
  <a class="lit">Read More &gt;</a>
</div>
<div class="abs svc" style="left:817px">
  <div class="icon"><svg width="72" height="64" viewBox="0 0 72 64" fill="#333"><rect x="34" y="2" width="4" height="9"/><path d="M14 30a22 22 0 0 1 44 0z"/><rect x="8" y="32" width="56" height="6"/><rect x="12" y="40" width="5" height="14"/><rect x="23" y="40" width="5" height="14"/><rect x="34" y="40" width="5" height="14"/><rect x="45" y="40" width="5" height="14"/><rect x="56" y="40" width="5" height="14"/><rect x="4" y="56" width="64" height="6"/></svg></div>
  <h3>GOVERNMENT</h3>
  <p>Lorem ipsum is simply dummy text of the printing and typeset-ting industry. Lorem Ipsum has been the industry's</p>
  <a>Read More &gt;</a>
</div>
<div class="btn consult">Free Consultation</div>

<!-- Projects -->
<div class="photo pillar-photo" role="img" aria-label="Photo of pale marble columns and a polished floor"></div>
<div class="abs sec-head projects-head"><div class="rule"></div><h2 class="display">Our <em>Projects</em></h2></div>
<p class="abs projects-copy">Lorem Ipsum is simply dummy text of <strong>the printing and type-setting industry</strong>. Lorem Ipsum has been</p>
<div class="photo project-a" role="img" aria-label="Photo of a school hallway with lockers and checkered tile floor"></div>
<div class="photo project-b" role="img" aria-label="Photo of a bright hospital corridor with a glossy floor"></div>
<div class="btn view-more">View More Projects</div>

<!-- Footer -->
<footer class="abs footer"></footer>
<div class="abs foot-divider" style="left:367px"></div>
<div class="abs foot-divider" style="left:655px"></div>
<div class="abs foot-divider" style="left:983px"></div>
<div class="abs foot-brand"><div class="dot"></div><span>Corvane Flooring</span></div>

<h4 class="abs foot-h" style="left:368px">Contact Us</h4>
<ul class="abs foot-contact">
  <li><svg width="18" height="22" viewBox="0 0 18 22"><path d="M9 0a8 8 0 0 1 8 8c0 6-8 14-8 14S1 14 1 8a8 8 0 0 1 8-8z" fill="#e8363d"/><circle cx="9" cy="8" r="3" fill="#4a4c4b"/></svg><span>Corvane Flooring<br>27 Marden Court, Lodi, CA 95240 United States</span></li>
  <li><svg width="18" height="18" viewBox="0 0 18 18"><path d="M4 1l3 4-2 2c1 3 3 5 6 6l2-2 4 3-2 3C8 17 1 10 1 3z" fill="#e8363d"/></svg><span>Phone:<br>0198 274 5530 and<br>+455 3107 2286</span></li>
  <li><svg width="18" height="14" viewBox="0 0 18 14"><rect width="18" height="14" rx="2" fill="#e8363d"/><path d="M1 2l8 6 8-6" stroke="#4a4c4b" stroke-width="1.6" fill="none"/></svg><span>Email:<br>hello@corvane.example</span></li>
</ul>

<h4 class="abs foot-h" style="left:655px">Sign Up For Newsletter</h4>
<p class="abs foot-news">excepteur sint occaecat cupidatat non proident, sunt in culpa qui</p>
<div class="abs email-field">Enter email</div>
<div class="btn subscribe">Subscribe</div>

<h4 class="abs foot-h" style="left:983px">Quick Links</h4>
<ul class="abs quick"><li>Home</li><li>About</li><li>Services</li><li>News</li><li>Contact Us</li></ul>

<div class="abs bottom"></div>
<div class="abs bottom-social" aria-label="Social links"><i></i><i style="background:#c23b8c"></i><i style="background:#2b9ae6"></i><i style="background:#1f6fb5"></i></div>
<p class="abs legal">Corvane Flooring © 2023 All Rights Reserved | Privacy Policy | Terms and Conditions</p>
<div class="abs red-band"></div>

</body>
</html>
```